Website for UK Fintech Company specialising in Auto-Finance asset management

We need a website for a FINTECH business called KELVO Asset Management. We have developed and licenced an innovative platform to provide financial institutions whom provide secured Asset finance loans to consumer and commercial clients, allowing for real time tracking and management of defaulted accounts pending repossession. The KELVO Asset Management platform is a total recoveries solution through the cycle, from the moment the lender has to recover the vehicle (due to default/non-payment) to the disposal of the vehicle (via sale at Motor Auctions or by selling to a Car dealership network). The data provided from external services allows the Financier to make informed decisions, such as whether it is economical to continue the recovery and decide which sales channel is better suited for their assets to maximise residual values and minimise financial losses. The KELVO platform provides an array of MI reporting and uses a systematic approach utilising exception reporting to identify key areas of non-performance to enable focus where needed. KELVO also provides a leading Debt collection service recovering end-of-cycle losses such as Financial Shortfall and losses in vehicle values due to conditions and excessive damage.

We also require a new logo for out new product called PL-Certify

Target Market(s)

Financial institutions whom provide secured Asset finance loans to consumer and commercial clients

Industry/Entity Type

Financial Service

Logo Text

PL- Certify (this is for a new product which forms part of the KELVO Asset Mangement Platform

Number of Pages Required

4 page

Font styles to use
Serif
Sans Serif

Colors

Designer to choose colors to be used in the design.

Requirements
Must have
• We need a simple website with a broken down as follows;
• • Landing page
• • Services page
• • About us page
• • KELVO Asset Management Platform login page (client facing)
Nice to have
• Our slogan is 'Auto-Finance Expertise'
• We are very much open to suggestions as long as we can create a professional/ corporate / modern feel to the website. We are a FINTECH company, and that needs to come across
Should not have
• Whilst we are an asset management company primarily managing vehicles through our platform, we don't want it to look like a car dealership website!:)

```html
<!DOCTYPE html>
<html lang="en">
<head>
<meta charset="utf-8">
<title>KELVO Asset Management Platform</title>
<link href="https://fonts.googleapis.com/css2?family=Open+Sans:wght@600;700;800&family=Roboto:wght@400;500;700&family=Montserrat:wght@600;700&display=swap" rel="stylesheet">
<style>
:root{
  --orange:#f07c00;
  --ink:#111111;
  --text:#333333;
  --muted:#8a8a8a;
  --line:#cfcfcf;
  --dark:#1f1f1f;
  --navy:#1d2b4a;
  --paper:#ffffff;
  --soft:#f1f1f1;
}
*{box-sizing:border-box;margin:0;padding:0}
html,body{width:1200px;height:2177px;overflow:hidden;background:var(--paper)}
body{position:relative;font-family:"Roboto",Arial,sans-serif;color:var(--text)}
.abs{position:absolute}

/* header */
.site-header{left:0;top:0;width:1200px;height:77px;background:var(--paper)}
.brand{left:160px;top:14px}
.brand-name{font:700 36px/1 "Roboto",sans-serif;color:var(--ink);display:flex;align-items:center;gap:6px}
.brand-name i{display:inline-block;width:10px;height:10px;background:var(--orange)}
.brand-tag{font:700 8px/1 "Roboto",sans-serif;color:var(--orange);margin-top:5px;letter-spacing:.2px}
.main-nav{right:158px;top:28px;display:flex;align-items:center;gap:28px;font:500 11px/1 "Roboto",sans-serif;color:#333;text-transform:uppercase}
.main-nav .home{position:relative}
.main-nav .home::before{content:"";position:absolute;left:-7px;top:-28px;width:36px;height:3px;background:var(--orange)}
.main-nav .login{font-weight:700;display:flex;align-items:center;gap:8px}

/* hero */
.hero{left:0;top:77px;width:1200px;height:505px;overflow:hidden}
.hero-photo{position:absolute;inset:0;background:linear-gradient(90deg,#c9d0d8 0%,#eef1f4 20%,#dfe5eb 45%,#c8d1da 60%,#eef1f4 80%,#c4ccd4 100%)}
.hero-title{position:absolute;left:0;top:345px;width:1200px;text-align:center;font:800 76px/1 "Open Sans",sans-serif;letter-spacing:9px;color:#000;white-space:nowrap}
.hero-band{position:absolute;left:0;top:420px;width:1200px;height:85px;background:rgba(40,44,50,.72)}
.hero-sub{position:absolute;left:0;top:438px;width:1200px;text-align:center;font:700 15px/1 "Montserrat",sans-serif;letter-spacing:2px;color:#fff}
.hero-more{position:absolute;left:0;top:470px;width:1200px;text-align:center;font:600 13px/1 "Open Sans",sans-serif;color:#fff}

/* section title tag */
.tag{height:40px;padding:0 24px;background:var(--ink);color:#fff;font:700 17px/40px "Roboto",sans-serif;border-bottom:3px solid var(--orange);white-space:nowrap}

/* services */
.services-deco{left:205px;top:672px;width:995px;height:285px;background:linear-gradient(90deg,rgba(200,210,220,.18),rgba(230,235,240,.25));}
.service-card{top:759px;width:158px;height:100px;border:1px dashed var(--line);background:rgba(255,255,255,.85);padding:14px 16px}
.service-card h3{font:500 18px/1 "Roboto",sans-serif;color:var(--ink)}
.service-card p{font:400 11px/1 "Roboto",sans-serif;color:#666;margin-top:12px}
.service-card a{display:block;font:700 10px/1 "Roboto",sans-serif;color:var(--orange);margin-top:7px;text-decoration:none}
.more-link{left:160px;top:905px;font:700 11px/1 "Roboto",sans-serif;color:var(--navy);display:flex;align-items:center;gap:10px}

/* platform band */
.platform{left:0;top:1046px;width:1200px;height:448px;background:linear-gradient(160deg,#3a3f49 0%,#23272e 45%,#4a4f58 75%,#2b2f36 100%)}
.platform-frame{left:184px;top:1087px;width:830px;height:366px;border:2px solid #fff}
.platform-title{left:466px;top:1136px;width:268px;height:39px;background:#fff;color:var(--ink);text-align:center;font:700 17px/39px "Roboto",sans-serif}
.platform-item{height:50px;border:1px dashed #fff;color:#fff;font:500 15px/50px "Roboto",sans-serif;text-align:center;white-space:nowrap}

/* about / news */
.headline{font:700 21px/1 "Roboto",sans-serif;color:var(--ink)}
.body-text{font:400 12px/19px "Roboto",sans-serif;color:#8a8a8a}
.product-bar{left:160px;top:1744px;width:307px;height:30px;background:var(--soft);border:1px solid #e3e3e3;font:700 13px/28px "Roboto",sans-serif;color:var(--ink);padding-left:17px}
.product-mark{left:160px;top:1806px;display:flex;align-items:center;gap:10px;font:700 34px/1 "Roboto",sans-serif;color:var(--orange)}
.product-mark span{display:inline-block;width:26px;height:26px;border-radius:50%;background:var(--navy)}
.product-note{left:160px;top:1873px;width:380px;display:flex;align-items:center;justify-content:space-between;font:400 11px/1 "Roboto",sans-serif;color:#888}
.product-note b{font-weight:400;color:#222}
.news-meta{left:604px;top:1820px;font:500 12px/1 "Roboto",sans-serif;color:#222}
.news-meta em{font-style:normal;color:#999;font-weight:400}
.pager{top:1859px;width:26px;height:26px;border-radius:50%;display:flex;align-items:center;justify-content:center}

/* newsletter */
.rule{left:130px;top:1975px;width:1070px;height:1px;background:#ddd}
.news-label{left:160px;top:2015px;font:700 16px/1 "Roboto",sans-serif;letter-spacing:3px;color:var(--ink)}
.news-input{left:479px;top:2005px;width:451px;height:38px;border:1px solid #e2e2e2;font:400 11px/36px "Roboto",sans-serif;color:#999;padding-left:18px}
.news-btn{left:937px;top:2005px;width:103px;height:38px;background:var(--ink);color:#fff;text-align:center;font:700 13px/36px "Roboto",sans-serif;border-bottom:2px solid var(--orange)}

/* footer */
.footer{left:0;top:2077px;width:1200px;height:54px;background:var(--dark)}
.footer-links{left:160px;top:2093px;font:400 11px/1 "Roboto",sans-serif;color:#ccc;white-space:nowrap}
.footer-links i{font-style:normal;color:#888;margin:0 6px}
.social{top:2086px;display:flex;gap:10px;right:160px}
.social span{width:26px;height:26px;border:2px solid #fff;border-radius:50%}
.legal{top:2150px;font:400 11px/1 "Roboto",sans-serif;color:#333}
</style>
</head>
<body>

<header class="abs site-header">
  <div class="abs brand">
    <div class="brand-name">KELVO<i></i></div>
    <div class="brand-tag">ASSET MANAGEMENT PLATFORM</div>
  </div>
  <nav class="abs main-nav">
    <span class="home"><svg width="22" height="18" viewBox="0 0 22 18"><path d="M11 1 1 9h3v8h5v-5h4v5h5V9h3z" fill="#f07c00"/></svg></span>
    <span>About Us</span>
    <span>Services</span>
    <span>KELVO Asset Management</span>
    <span class="login">Login <svg width="16" height="17" viewBox="0 0 16 17"><circle cx="8" cy="5" r="4" fill="none" stroke="#333" stroke-width="1.5"/><path d="M1 16c0-4 3-6 7-6s7 2 7 6z" fill="none" stroke="#333" stroke-width="1.5"/></svg></span>
  </nav>
</header>

<section class="abs hero">
  <div class="hero-photo" role="img" aria-label="Bright glass-walled boardroom overlooking a city skyline"></div>
  <h1 class="hero-title">AUTO-FINANCE EXPERTISE</h1>
  <div class="hero-band"></div>
  <p class="hero-sub">FINTECH COMPANY SPECIALIZING IN AUTO-FINANCE ASSET MANAGEMENT</p>
  <p class="hero-more">More Information &#9656;</p>
</section>

<div class="abs services-deco" role="img" aria-label="Faint background photo of a business meeting"></div>
<div class="abs tag" style="left:160px;top:670px">KELVO SERVICES</div>

<article class="abs service-card" style="left:160px"><h3>Asset finance</h3><p>Lorem ipsum dolor...</p><a>GET STARTED</a></article>
<article class="abs service-card" style="left:338px"><h3>Auto-Finance</h3><p>Lorem ipsum dolor...</p><a>GET STARTED</a></article>
<article class="abs service-card" style="left:517px"><h3>Asset manag.</h3><p>Lorem ipsum dolor...</p><a>GET STARTED</a></article>
<article class="abs service-card" style="left:695px"><h3>loans</h3><p>Lorem ipsum dolor...</p><a>GET STARTED</a></article>
<article class="abs service-card" style="left:874px"><h3>Fintech</h3><p>Lorem ipsum dolor...</p><a>GET STARTED</a></article>

<div class="abs more-link">VIEW MORE SERVICES <svg width="6" height="8" viewBox="0 0 6 8"><path d="M0 0 6 4 0 8z" fill="#1d2b4a"/></svg></div>

<section class="abs platform" role="img" aria-label="Businessman in a suit working with a calculator at a desk"></section>
<div class="abs platform-frame"></div>
<div class="abs platform-title">KELVO ASSET MANAGEMENT</div>
<div class="abs platform-item" style="left:234px;top:1234px;width:229px">1 .&nbsp; Asset finance loans</div>
<div class="abs platform-item" style="left:488px;top:1234px;width:181px">2 . Auto-Finance</div>
<div class="abs platform-item" style="left:695px;top:1234px;width:270px">3 . Loans to commercial clients</div>
<div class="abs platform-item" style="left:312px;top:1329px;width:228px">4 . Asset Management</div>
<div class="abs platform-item" style="left:563px;top:1329px;width:325px">5 . Asset Finance Loans To Consumer</div>

<div class="abs tag" style="left:160px;top:1584px">ABOUT KELVO</div>
<h2 class="abs headline" style="left:160px;top:1654px">Lorem ipsum dolor sit amet, consectetur</h2>
<p class="abs body-text" style="left:160px;top:1684px;width:380px">Lorem ipsum dolor sit amet, consectetur adipiscing elit, sed do eiusmod tempor incididunt ut labore et dolore magna aliqua. Ut enim ad minim</p>
<div class="abs product-bar">OUR NEW PRODUCT</div>
<div class="abs product-mark"><span></span>PL-Certify</div>
<div class="abs product-note"><span><span style="color:#f07c00">&#10003;</span>&nbsp; Lorem ipsum dolor sit amet, consectetur adipiscing elit.</span><b>Read More..</b></div>

<div class="abs tag" style="left:604px;top:1584px">NEWS &amp; UPDATES</div>
<h2 class="abs headline" style="left:604px;top:1654px">Lorem ipsum dolor sit amet,</h2>
<p class="abs body-text" style="left:604px;top:1694px;width:440px">Lorem ipsum dolor sit amet, consectetur adipiscing elit, sed do eiusmod tempor incididunt ut labore et dolore magna aliqua. Ut enim ad minim veniam, quis nostrud exercitation ullamco laboris nisi ut aliquip.</p>
<p class="abs body-text" style="left:604px;top:1771px;width:440px">Duis aute irure dolor in reprehenderit in voluptate velit esse cillum dolore eu</p>
<div class="abs news-meta">Lorem Ipsum Dolor &nbsp;|&nbsp; <em>February 27, 2018</em></div>
<div class="abs pager" style="left:602px;background:var(--orange)"><svg width="6" height="8" viewBox="0 0 6 8"><path d="M6 0 0 4 6 8z" fill="#fff"/></svg></div>
<div class="abs pager" style="left:634px;background:#eee"><svg width="6" height="8" viewBox="0 0 6 8"><path d="M0 0 6 4 0 8z" fill="#222"/></svg></div>

<div class="abs rule"></div>
<div class="abs news-label">SUBSCRIBE OUR NEWSLETTER :</div>
<div class="abs news-input">Enter your email id</div>
<div class="abs news-btn">SIGN UP</div>

<footer class="abs footer"></footer>
<div class="abs footer-links">Home<i>/</i>About Us<i>/</i>Services<i>/</i>KELVO Asset Management<i>/</i>Login<i>/</i>Contact Us</div>
<div class="abs social"><span></span><span></span><span></span><span></span></div>
<div class="abs legal" style="left:160px">© Copyright 2018 &nbsp;KELVO Asset Management Platform, All Rights Reserved</div>
<div class="abs legal" style="right:160px">Privacy Policy &nbsp;/&nbsp; Terms of Service</div>

</body>
</html>
```